Mossy Den Pet Supply

Thank you for your interest in this design contest. We are always welcome to questions and are looking forward to seeing what you can come up with.

We work on a Bootstrap platform with our custom built CMS. We require all designs to be sized accordingly with the bootstrap grid system found here: http://fernlattice.com/css/#grid

At the start of a competition, we are looking for general Home Page Design concepts and an example product grid page.

Homepage: Slide Show/Featured Products/Specials

example website as a reference:https://www.mintcollarworks.com/

Store Product Grid: Show a grid of product thumbnails. Included elements are thumbnail and price. Also included are filters (sort by, show by grid/list).

No photos at this time but Logo is attached. Looking for good quality photo's around the web. Please read the attached creative brief in depth to get an idea f what the client is looking for. Thanks!

```html
<!DOCTYPE html>
<html lang="en">
<head>
<meta charset="utf-8">
<title>Mossy Den Pet Supply</title>
<link href="https://fonts.googleapis.com/css2?family=Open+Sans:wght@300;400;600;700&display=swap" rel="stylesheet">
<style>
:root{
  --green:#8cc63f;
  --green-dark:#6f9e2c;
  --topbar:#787878;
  --topbar-line:#8a8a8a;
  --ink:#333;
  --ink-soft:#555;
  --muted:#777;
  --white:#fff;
  --social:#5c5c5c;
}
*{margin:0;padding:0;box-sizing:border-box}
html,body{width:901px;height:1200px;overflow:hidden;background:var(--white)}
body{font-family:'Open Sans',Arial,sans-serif;color:var(--ink);position:relative}
a{color:inherit;text-decoration:none}

.topbar{position:absolute;left:0;top:0;width:901px;height:35px;background:var(--topbar)}
.topbar__nav{position:absolute;left:427px;top:0;height:35px;display:flex}
.topbar__item{height:35px;border-left:1px solid var(--topbar-line);color:var(--white);font-size:10px;font-weight:600;display:flex;align-items:center;justify-content:center}
.topbar__home{width:36px;background:#6c6c6c}
.topbar__social{position:absolute;left:802px;top:0;width:99px;height:35px;background:#9b9b9b;display:flex;gap:3px;align-items:center;padding-left:10px}
.social-square{width:21px;height:21px;background:var(--social);border-radius:2px}

.logo{position:absolute;left:16px;top:0;width:102px;height:119px;background:var(--white);display:flex;flex-direction:column;align-items:center;justify-content:flex-end;padding-bottom:8px;z-index:2}
.logo__mark{width:40px;height:40px;background:var(--ink);border-radius:50%;margin-bottom:8px}
.logo__name{font-size:12px;font-weight:700;color:var(--ink);text-align:center;line-height:1.15}

.header__call{position:absolute;right:17px;top:58px;font-size:21px;font-weight:300;color:var(--muted)}
.header__links{position:absolute;right:17px;top:90px;font-size:9px;color:var(--muted);letter-spacing:.2px}
.header__links span{margin:0 4px}

.mainnav{position:absolute;left:0;top:126px;width:901px;height:35px;background:var(--green);display:flex}
.mainnav__item{height:35px;display:flex;align-items:center;padding:0 11px 0 9px;color:var(--white);font-size:11px;font-weight:600;border-right:1px solid #a3d264}
.paw{width:14px;height:14px;margin-right:6px;flex:none}

.hero{position:absolute;left:0;top:161px;width:901px;height:395px;background:linear-gradient(160deg,#8e8170 0%,#b4a48c 25%,#d2703a 55%,#e9e2d2 75%,#c55a2c 100%)}
.hero__arrow{position:absolute;top:170px;width:36px;height:35px;background:rgba(140,198,63,.75);display:flex;align-items:center;justify-content:center}
.hero__arrow--prev{left:16px}
.hero__arrow--next{left:850px}
.hero__caption{position:absolute;left:128px;top:211px;width:395px;height:63px;background:rgba(40,40,40,.72);padding:3px 8px;color:var(--white)}
.hero__title{font-size:24px;font-weight:600;line-height:1.2}
.hero__sub{font-size:18px;font-weight:300;line-height:1.2}

.card{position:absolute;top:579px;width:240px;height:247px;background:linear-gradient(#ececec,#ffffff 85%,#efefef)}
.card__photo{position:absolute;left:14px;top:14px;width:212px;height:108px}
.card__label{position:absolute;left:-10px;top:132px;width:207px;height:42px}
.card__title{position:absolute;left:24px;top:0;height:42px;display:flex;align-items:center;color:var(--white);font-size:19px;font-weight:300}
.card__text{position:absolute;left:16px;top:189px;font-size:11px;line-height:14px;color:var(--ink-soft);width:215px}
.card__link{position:absolute;left:17px;top:218px;font-size:12px;font-weight:700;color:var(--green);text-decoration:underline}

.about{position:absolute;left:0;top:847px;width:901px;height:246px;background:var(--green)}
.about__photo{position:absolute;left:0;top:0;width:470px;height:246px;background:linear-gradient(90deg,#a9ca74 0%,#8fa85f 45%,#9cc45c 80%,var(--green) 100%)}
.about__title{position:absolute;left:474px;top:48px;font-size:31px;font-weight:300;color:var(--white)}
.about__text{position:absolute;left:474px;top:90px;width:360px;font-size:10px;line-height:12.8px;color:var(--white);font-weight:300}
.about__btn{position:absolute;left:474px;top:179px;width:77px;height:25px;background:var(--white);border-radius:2px;font-size:9px;color:var(--ink-soft);display:flex;align-items:center;justify-content:center}

.footer{position:absolute;left:0;top:1093px;width:901px;height:107px}
.footer__pay-title{position:absolute;left:18px;top:13px;font-size:10.5px;font-weight:600;color:var(--ink-soft)}
.footer__cards{position:absolute;left:18px;top:31px;display:flex;gap:4px}
.pay-chip{width:24px;height:14px;border:1px solid #ccc;background:#e6e6e6}
.footer__links{position:absolute;left:18px;top:59px;font-size:10.5px;color:var(--ink-soft)}
.footer__copy{position:absolute;left:18px;top:77px;font-size:9px;color:var(--muted)}
.footer__copy a{text-decoration:underline;margin:0 6px}
.footer__social{position:absolute;left:687px;top:68px;display:flex;gap:2px}
.footer__social .social-square{width:22px;height:22px;background:#6a6a6a}
.footer__logo{position:absolute;left:772px;top:12px;width:92px;display:flex;flex-direction:column;align-items:center}
.footer__logo .logo__mark{background:#8a8a8a;width:34px;height:34px;margin-bottom:6px}
.footer__logo .logo__name{color:#8a8a8a;font-size:11px}
</style>
</head>
<body>

<header>
  <div class="topbar">
    <nav class="topbar__nav">
      <a class="topbar__item topbar__home" href="#" aria-label="Home">
        <svg width="18" height="18" viewBox="0 0 18 18"><path d="M9 2 L17 9 H14.5 V16 H10.5 V11.5 H7.5 V16 H3.5 V9 H1 Z" fill="#8cc63f"/></svg>
      </a>
      <a class="topbar__item" style="width:83px" href="#">Sign In</a>
      <a class="topbar__item" style="width:84px" href="#">Register</a>
      <a class="topbar__item" style="width:84px" href="#">Wish List</a>
      <a class="topbar__item" style="width:88px" href="#">Shopping Cart</a>
    </nav>
    <div class="topbar__social">
      <span class="social-square"></span><span class="social-square"></span><span class="social-square"></span>
    </div>
  </div>

  <a class="logo" href="#">
    <span class="logo__mark"></span>
    <span class="logo__name">MOSSY DEN<br>PET SUPPLY</span>
  </a>

  <div class="header__call">Buy Online or Call : 0000 000 0000</div>
  <div class="header__links">Blog<span>|</span>E-commerce<span>|</span>Reservations<span>|</span>Event Calendar<span>|</span>News</div>

  <nav class="mainnav">
    <a class="mainnav__item" href="#"><svg class="paw" viewBox="0 0 14 14"><g fill="#fff"><ellipse cx="7" cy="9.5" rx="3.3" ry="3"/><circle cx="2.2" cy="6" r="1.5"/><circle cx="4.8" cy="2.6" r="1.5"/><circle cx="9.2" cy="2.6" r="1.5"/><circle cx="11.8" cy="6" r="1.5"/></g></svg>Dog Products</a>
    <a class="mainnav__item" href="#"><svg class="paw" viewBox="0 0 14 14"><g fill="#fff"><ellipse cx="7" cy="9.5" rx="3.3" ry="3"/><circle cx="2.2" cy="6" r="1.5"/><circle cx="4.8" cy="2.6" r="1.5"/><circle cx="9.2" cy="2.6" r="1.5"/><circle cx="11.8" cy="6" r="1.5"/></g></svg>Pupy Products</a>
    <a class="mainnav__item" href="#"><svg class="paw" viewBox="0 0 14 14"><g fill="#fff"><ellipse cx="7" cy="9.5" rx="3.3" ry="3"/><circle cx="2.2" cy="6" r="1.5"/><circle cx="4.8" cy="2.6" r="1.5"/><circle cx="9.2" cy="2.6" r="1.5"/><circle cx="11.8" cy="6" r="1.5"/></g></svg>Dealer</a>
    <a class="mainnav__item" href="#"><svg class="paw" viewBox="0 0 14 14"><g fill="#fff"><ellipse cx="7" cy="9.5" rx="3.3" ry="3"/><circle cx="2.2" cy="6" r="1.5"/><circle cx="4.8" cy="2.6" r="1.5"/><circle cx="9.2" cy="2.6" r="1.5"/><circle cx="11.8" cy="6" r="1.5"/></g></svg>Retailer</a>
    <a class="mainnav__item" href="#"><svg class="paw" viewBox="0 0 14 14"><g fill="#fff"><ellipse cx="7" cy="9.5" rx="3.3" ry="3"/><circle cx="2.2" cy="6" r="1.5"/><circle cx="4.8" cy="2.6" r="1.5"/><circle cx="9.2" cy="2.6" r="1.5"/><circle cx="11.8" cy="6" r="1.5"/></g></svg>Customer Locator</a>
    <a class="mainnav__item" href="#"><svg class="paw" viewBox="0 0 14 14"><g fill="#fff"><ellipse cx="7" cy="9.5" rx="3.3" ry="3"/><circle cx="2.2" cy="6" r="1.5"/><circle cx="4.8" cy="2.6" r="1.5"/><circle cx="9.2" cy="2.6" r="1.5"/><circle cx="11.8" cy="6" r="1.5"/></g></svg>Photo Galleries</a>
    <a class="mainnav__item" href="#" style="border-right:none"><svg class="paw" viewBox="0 0 14 14"><g fill="#fff"><ellipse cx="7" cy="9.5" rx="3.3" ry="3"/><circle cx="2.2" cy="6" r="1.5"/><circle cx="4.8" cy="2.6" r="1.5"/><circle cx="9.2" cy="2.6" r="1.5"/><circle cx="11.8" cy="6" r="1.5"/></g></svg>Video Galleries</a>
  </nav>
</header>

<main>
  <section class="hero" role="img" aria-label="Photo of a pale labrador resting on an orange patterned dog bed by a sunny window">
    <a class="hero__arrow hero__arrow--prev" href="#" aria-label="Previous slide"><svg width="14" height="20" viewBox="0 0 14 20"><path d="M12 2 L3 10 L12 18" stroke="#444" stroke-width="2.5" fill="none"/></svg></a>
    <a class="hero__arrow hero__arrow--next" href="#" aria-label="Next slide"><svg width="14" height="20" viewBox="0 0 14 20"><path d="M2 2 L11 10 L2 18" stroke="#444" stroke-width="2.5" fill="none"/></svg></a>
    <div class="hero__caption">
      <div class="hero__title">Dog Beds</div>
      <div class="hero__sub">Stylish, comfortable and made in the USA</div>
    </div>
  </section>

  <article class="card" style="left:62px">
    <div class="card__photo" role="img" aria-label="Photo of a brown puppy lying in a pink dog bed" style="background:linear-gradient(135deg,#7a5236,#c98e62 45%,#d9c7c9)"></div>
    <svg class="card__label" viewBox="0 0 207 42"><polygon points="0,0 10,-9 10,0" fill="#557d20"/><polygon points="0,0 183,0 207,21 183,42 0,42" fill="#8cc63f"/></svg>
    <div class="card__title" style="left:14px;top:132px"><svg class="paw" viewBox="0 0 14 14"><g fill="#fff"><ellipse cx="7" cy="9.5" rx="3.3" ry="3"/><circle cx="2.2" cy="6" r="1.5"/><circle cx="4.8" cy="2.6" r="1.5"/><circle cx="9.2" cy="2.6" r="1.5"/><circle cx="11.8" cy="6" r="1.5"/></g></svg>Dog Beds</div>
    <p class="card__text">Sample Text Sample Text Sample Text Sample Text Sample Text Sample Text</p>
    <a class="card__link" href="#">Click Here</a>
  </article>

  <article class="card" style="left:326px">
    <div class="card__photo" role="img" aria-label="Photo of a dark brindle dog wearing a chain leash" style="background:linear-gradient(135deg,#6f7060,#4a4a48 50%,#8c7e6a)"></div>
    <svg class="card__label" viewBox="0 0 207 42"><polygon points="0,0 183,0 207,21 183,42 0,42" fill="#8cc63f"/></svg>
    <div class="card__title" style="left:14px;top:132px"><svg class="paw" viewBox="0 0 14 14"><g fill="#fff"><ellipse cx="7" cy="9.5" rx="3.3" ry="3"/><circle cx="2.2" cy="6" r="1.5"/><circle cx="4.8" cy="2.6" r="1.5"/><circle cx="9.2" cy="2.6" r="1.5"/><circle cx="11.8" cy="6" r="1.5"/></g></svg>Dog Leashes</div>
    <p class="card__text">Sample Text Sample Text Sample Text Sample Text Sample Text Sample Text</p>
    <a class="card__link" href="#">Click Here</a>
  </article>

  <article class="card" style="left:590px">
    <div class="card__photo" role="img" aria-label="Photo of a blue beaded collar on a tan dog" style="background:linear-gradient(135deg,#8a5a36,#b7814f 50%,#eae4de)"></div>
    <svg class="card__label" viewBox="0 0 207 42"><polygon points="0,0 183,0 207,21 183,42 0,42" fill="#8cc63f"/></svg>
    <div class="card__title" style="left:14px;top:132px"><svg class="paw" viewBox="0 0 14 14"><g fill="#fff"><ellipse cx="7" cy="9.5" rx="3.3" ry="3"/><circle cx="2.2" cy="6" r="1.5"/><circle cx="4.8" cy="2.6" r="1.5"/><circle cx="9.2" cy="2.6" r="1.5"/><circle cx="11.8" cy="6" r="1.5"/></g></svg>Dog Collars</div>
    <p class="card__text">Sample Text Sample Text Sample Text Sample Text Sample Text Sample Text</p>
    <a class="card__link" href="#">Click Here</a>
  </article>

  <section class="about">
    <div class="about__photo" role="img" aria-label="Green-tinted photo of a black labrador lying on a sofa"></div>
    <h2 class="about__title">Mossy Den Pet Supply</h2>
    <p class="about__text">Sample text sample text sample text sample text sample text sample text sample text sample text sample text sample text sample text sample text sample text sample text sample text sample text sample text sample text sample text sample text sample text sample text sample text sample text sample text sample text sample text sample text sample text sample text sample text sample text sample text sample text sample text.</p>
    <a class="about__btn" href="#">Learn more...</a>
  </section>
</main>

<footer class="footer">
  <div class="footer__pay-title">PAYMENT OPTIONS</div>
  <div class="footer__cards">
    <span class="pay-chip"></span><span class="pay-chip"></span><span class="pay-chip"></span><span class="pay-chip"></span><span class="pay-chip"></span>
  </div>
  <div class="footer__links">Home | Dog Products | Pupy Products | Dealer | Retailer | Customer Locator | Photo Galleries | Video Galleries</div>
  <div class="footer__copy">© Mossy Den Pet Supply. All Rights Reserved. <a href="#">Terms &amp; Conditions</a>|<a href="#">Privacy Statement</a></div>
  <div class="footer__social"><span class="social-square"></span><span class="social-square"></span><span class="social-square"></span></div>
  <div class="footer__logo">
    <span class="logo__mark"></span>
    <span class="logo__name">MOSSY DEN<br>PET SUPPLY</span>
  </div>
</footer>

</body>
</html>
```